roomhavenly.net banner ads

Hi All,

I'm looking for a set of banner ads designing for a Quorvix Promoads campaign for roomhavenly.net.

The website serves the UK and is a portal for people who cannot afford to buy or rent a place of their own, to find a room to let in someone else's house.

Conversely, home owners can pay to advertise a listing of their spare room. Have a look at the site, and you'll get the idea. Please bear in mind that it's a work in progress and is currently being developed and polished.

The banners do not have to be animated (no Flash please) but should cover all the standard sizes used by Quorvix Promoads.

Please take design guidance and inspiration from the web site itself. I'm looking for something eye-catching and creative.

Many thanks,
Leon

Target Market(s)

1. People who can't afford to buy or rent a property

Industry/Entity Type

House

Requirements
Must have
• The logo should be prominent in the ads

```html
<!DOCTYPE html>
<html lang="en">
<head>
<meta charset="utf-8">
<title>roomhavenly.net – Latest rooms banner</title>
<link rel="stylesheet" href="https://fonts.googleapis.com/css2?family=Arimo:wght@400;700&display=swap">
<style>
  :root {
    --bar-dark: #2b2b2b;
    --bar-text: #ffffff;
    --panel-bg: #f3f4f5;
    --panel-edge: #d5d8db;
    --accent-blue: #1d6fb8;
    --title-orange: #e86f0c;
    --body-grey: #555a5e;
    --btn-top: #f59a2c;
    --btn-bottom: #e0700a;
    --btn-edge: #c25c05;
    --btn-dot: #3a2a1c;
    --photo-top: #c7a0a8;
    --photo-bottom: #6b5a60;
  }
  * { box-sizing: border-box; margin: 0; padding: 0; }
  html, body { width: 1200px; height: 148px; overflow: hidden; background: #ffffff; }
  body { font-family: "Arimo", Arial, sans-serif; }

  .banner { position: relative; width: 1200px; height: 148px; background: var(--panel-bg); border: 1px solid var(--panel-edge); overflow: hidden; }

  .headline-bar { position: absolute; left: 0; top: 0; width: 100%; height: 20px; background: var(--bar-dark); color: var(--bar-text); font-size: 15px; line-height: 20px; text-align: center; }

  .room-photo { position: absolute; left: 0; top: 20px; width: 248px; height: 128px; background: linear-gradient(135deg, var(--photo-top), var(--photo-bottom)); }

  .accent-strip { position: absolute; left: 248px; top: 20px; width: 10px; height: 128px; background: var(--accent-blue); }

  .listing { position: absolute; left: 292px; top: 30px; width: 620px; }
  .listing-title { color: var(--title-orange); font-weight: 700; font-size: 24px; line-height: 30px; white-space: nowrap; }
  .listing-text { color: var(--body-grey); font-size: 18px; line-height: 23px; margin-top: 2px; }
  .listing-more { color: var(--title-orange); }

  .listing-price { position: absolute; left: 610px; top: 112px; color: var(--body-grey); font-size: 20px; }

  .cta { position: absolute; left: 936px; top: 36px; width: 252px; height: 52px; border-radius: 6px; border: 1px solid var(--btn-edge); background: linear-gradient(var(--btn-top), var(--btn-bottom)); color: #ffffff; font-weight: 700; font-size: 21px; display: flex; align-items: center; padding-left: 22px; }
  .cta svg { position: absolute; right: 14px; top: 11px; }

  .brand { position: absolute; left: 952px; top: 102px; display: flex; align-items: center; gap: 8px; color: var(--accent-blue); font-weight: 700; font-size: 27px; }
  .brand-square { width: 24px; height: 24px; background: var(--accent-blue); }
</style>
</head>
<body>
<div class="banner">
  <div class="headline-bar">Latest rooms in and around London</div>
  <div class="room-photo" role="img" aria-label="Photo of the double room with bed and dresser"></div>
  <div class="accent-strip"></div>

  <div class="listing">
    <p class="listing-title">Double Room available for rent in Fulham</p>
    <p class="listing-text">Hi, after over 2 years in this great flat, I'm moving out to<br><span class="listing-more">More...</span></p>
  </div>
  <p class="listing-price">US$330, Double room</p>

  <div class="cta">Find Out More
    <svg width="30" height="30" viewBox="0 0 30 30" aria-hidden="true">
      <circle cx="15" cy="15" r="14" fill="var(--btn-dot)"/>
      <path d="M12 9 L20 15 L12 21 Z" fill="var(--btn-top)"/>
    </svg>
  </div>

  <div class="brand"><span class="brand-square"></span>roomhavenly.net</div>
</div>
</body>
</html>
```